Tobin's Jewelry Studio Needs a Moving Location Flyer

We need a flyer to inform our customers of our location moving. We will be moving to our city's downtown which is only 1 mile away from our current address. We will be having a moving sale ( Up to 80% off). The sale starts Sept. 8th Our business creates, sells, and repairs fine jewelry. Dimensions are 5"x8"

Target Market(s)

Women ages 25-55

Industry/Entity Type

Jewelry

Colors
85abd2
cfdeed

Requirements
Must have
• Our logo
• Mention of the sale
• Our current address
• 4785 Cresthaven Blvd.
• Dunmore, Ca 94318
• (415)826-3319
Nice to have
• Mention that we're relocating to downtown Dunmore (new location opening Nov. 1st.)

```html
<!DOCTYPE html>
<html lang="en">
<head>
<meta charset="utf-8">
<title>Tobin's Jewelry Studio – Moving Sale Flyer</title>
<link href="https://fonts.googleapis.com/css2?family=Roboto+Condensed:wght@400;700&family=Varela+Round&display=swap" rel="stylesheet">
<style>
  :root {
    --page: #eef2f4;
    --card-top: #ffffff;
    --card-edge: #bfe3ea;
    --circle-fill: #c3e6ec;
    --circle-ring: #ffffff;
    --circle-outline: #a9dbe3;
    --brown: #4a1a14;
    --teal: #137586;
    --tagline: #85abd2;
    --wave-light: #cfdeed;
    --wave-deep: #4fa2dc;
  }
  * { box-sizing: border-box; margin: 0; padding: 0; }
  html, body { width: 1200px; height: 1200px; overflow: hidden; }
  body {
    background: var(--page);
    font-family: "Roboto Condensed", "Arial Narrow", sans-serif;
    position: relative;
  }
  .flyer {
    position: absolute;
    left: 30px; top: 231px;
    width: 1140px; height: 737px;
    overflow: hidden;
    background: radial-gradient(ellipse at 50% 30%, var(--card-top) 0%, #eaf7f9 45%, var(--card-edge) 100%);
    box-shadow: 0 10px 30px rgba(0,0,0,.18);
  }
  .flyer__wave {
    position: absolute;
    left: 0; top: 300px; width: 1140px; height: 437px;
    background:
      radial-gradient(ellipse 70% 28% at 30% 48%, rgba(79,162,220,.55), rgba(79,162,220,0) 70%),
      radial-gradient(ellipse 40% 25% at 85% 22%, rgba(79,162,220,.45), rgba(79,162,220,0) 70%),
      linear-gradient(180deg, rgba(207,222,237,0) 0%, rgba(207,222,237,.5) 45%, rgba(255,255,255,.85) 100%);
  }
  .brand {
    position: absolute;
    left: 0; top: 124px; width: 1140px; height: 60px;
  }
  .brand__rule {
    position: absolute; top: 28px; height: 4px; width: 70px;
    background: var(--brown);
  }
  .brand__rule--left { left: 210px; }
  .brand__rule--right { right: 186px; }
  .brand__mark {
    position: absolute; left: 320px; top: 6px;
    width: 48px; height: 48px; border-radius: 50%;
    background: var(--circle-fill);
    border: 3px solid var(--circle-ring);
    box-shadow: 0 0 0 1px var(--circle-outline);
  }
  .brand__name {
    position: absolute; left: 384px; top: 4px;
    font-size: 44px; font-weight: 700; color: var(--brown);
    letter-spacing: 1px; line-height: 52px;
  }
  .tagline {
    position: absolute; left: 0; top: 250px; width: 1140px;
    text-align: center;
    font-family: "Varela Round", sans-serif;
    font-size: 38px; color: var(--tagline);
    letter-spacing: -1.5px;
  }
  .badge {
    position: absolute; top: 316px;
    width: 338px; height: 338px; border-radius: 50%;
    background: var(--circle-fill);
    border: 5px solid var(--circle-ring);
    box-shadow: 0 0 0 2px var(--circle-outline);
    display: flex; flex-direction: column; align-items: center; justify-content: center;
    text-align: center;
  }
  .badge--relocation { left: 63px; }
  .badge--sale { left: 407px; }
  .badge--details { left: 748px; }

  .relocation__lead { font-size: 35px; line-height: 36px; color: var(--brown); margin-top: 2px; }
  .relocation__city { font-size: 52px; line-height: 54px; color: var(--brown); }
  .relocation__opening {
    width: 290px; margin: 4px 0 6px;
    background: linear-gradient(90deg, rgba(255,255,255,0), rgba(255,255,255,.9) 20%, rgba(255,255,255,.9) 80%, rgba(255,255,255,0));
    font-size: 23px; line-height: 38px; font-weight: 700; color: var(--teal);
  }
  .relocation__distance { font-size: 26px; line-height: 32px; color: var(--teal); }
  .relocation__distance strong { font-size: 35px; }

  .sale__moving { font-size: 70px; line-height: 66px; font-weight: 700; color: var(--brown); margin-top: 6px; }
  .sale__word {
    font-size: 108px; line-height: 96px; font-weight: 700; color: #fff;
    text-shadow: 3px 4px 6px rgba(0,0,0,.25);
  }
  .sale__offer {
    display: flex; align-items: center; gap: 2px;
    font-size: 36px; color: var(--brown); margin-top: 8px;
  }
  .sale__percent {
    width: 72px; height: 72px; border-radius: 50%;
    background: var(--brown); color: #fff;
    display: flex; align-items: center; justify-content: center;
    font-size: 33px;
  }

  .details__lead { font-size: 35px; line-height: 42px; color: var(--brown); }
  .details__date { font-size: 34px; line-height: 44px; font-weight: 700; color: var(--brown); margin-bottom: 6px; }
  .details__line { font-size: 32px; line-height: 40px; color: var(--teal); }
  .details__phone { font-size: 32px; line-height: 40px; font-weight: 700; color: var(--teal); }
</style>
</head>
<body>
  <main class="flyer">
    <div class="flyer__wave" role="img" aria-label="Soft flowing blue wave and fine diagonal line backdrop"></div>

    <header class="brand">
      <span class="brand__rule brand__rule--left"></span>
      <span class="brand__mark"></span>
      <h1 class="brand__name">Tobin's Jewelry Studio</h1>
      <span class="brand__rule brand__rule--right"></span>
    </header>

    <p class="tagline">creates, sells, and repairs fine jewelry</p>

    <section class="badge badge--relocation">
      <p class="relocation__lead">We're relocating<br>to downtown</p>
      <p class="relocation__city">Dunmore</p>
      <p class="relocation__opening">OPENING NOV. 1ST.</p>
      <p class="relocation__distance"><strong>1 mile</strong> away from<br>our current address</p>
    </section>

    <section class="badge badge--sale">
      <p class="sale__moving">MOVING</p>
      <p class="sale__word">SALE</p>
      <p class="sale__offer">UP TO <span class="sale__percent">80%</span> OFF</p>
    </section>

    <section class="badge badge--details">
      <p class="details__lead">The sale starts</p>
      <p class="details__date">Sept. 8th</p>
      <p class="details__line">4785 Cresthaven Blvd.</p>
      <p class="details__line">Dunmore, Ca 94318</p>
      <p class="details__phone">(415)826-3319</p>
    </section>
  </main>
</body>
</html>
```